TONVALE - A modern gin bottle label

Design of a bottle label in a modern fresh design. The name of the gin is "TONVALE Phantom Batch K7". Please take a look at the tonvale.de website. on the main page of tonvale.de you can breathe the design direction here: 1) the taste of the gin should be composed of 10 botanicals ... an important scent note. ) a distinctive flavor is spicy and fresh 3.) The filling volume is 0.5 liters 4.) the alcohol content is 43% vol. 5.) the variety is called "dry gin" 6.) tonvale stands for "energy" and "love"

Target Market(s)

Alcohol consumer

Colors

Designer to choose colors to be used in the design.

Requirements
Must have
• the tonvale corporate logo must be included, the name of the gin is "TONVALE Phantom Batch K7"
Nice to have
• Please use the bottles template in the appendix. (The Black Bottles) they can use the saying "DESTILLED & BOTTLED BY OLD MARINER" in small letters

```html
<!DOCTYPE html>
<html lang="en">
<head>
<meta charset="utf-8">
<title>TONVALE Phantom Batch K7 – Label</title>
<link rel="stylesheet" href="https://fonts.googleapis.com/css2?family=Oswald:wght@400;600;700&family=Roboto+Condensed:wght@300;400&family=Playfair+Display:wght@900&display=swap">
<style>
  :root {
    --backdrop: #141414;
    --label-border: #e2e2e2;
    --label-paper: #ffffff;
    --ink: #2a2a2a;
    --ink-soft: #3c3c3c;
    --rule: #d6d6d6;
    --accent: #f26a10;
  }
  * { margin: 0; padding: 0; box-sizing: border-box; }
  html, body {
    width: 777px; height: 1200px; overflow: hidden;
    background: var(--backdrop);
  }
  .canvas { position: relative; width: 777px; height: 1200px; }

  .label {
    position: absolute; left: 38px; top: 178px;
    width: 700px; height: 843px;
    background: var(--label-border);
  }
  .label-paper {
    position: absolute; left: 30px; top: 29px; right: 27px; bottom: 30px;
    background: var(--label-paper);
  }
  .frame-lines { position: absolute; left: 0; top: 0; width: 700px; height: 843px; }

  .brand {
    position: absolute; left: 0; width: 700px; top: 112px;
    text-align: center;
  }
  .brand-dot {
    display: block; width: 50px; height: 50px; margin: 0 auto 14px;
    border-radius: 50%; background: var(--accent);
  }
  .brand-name {
    font-family: "Oswald", sans-serif; font-weight: 600;
    font-size: 52px; line-height: 1; letter-spacing: 34px;
    color: var(--ink); padding-left: 34px;
  }

  .edition {
    position: absolute; left: 120px; top: 312px;
    font-family: "Oswald", sans-serif; font-weight: 700;
    font-size: 120px; line-height: 140px; letter-spacing: -2px;
    color: var(--ink); text-transform: uppercase;
  }
  .edition span { display: block; }

  .batch-badge {
    position: absolute; left: 522px; top: 582px;
    width: 90px; height: 90px; border-radius: 50%;
    background: var(--accent); color: var(--ink);
    font-family: "Playfair Display", serif; font-weight: 900;
    font-size: 44px; line-height: 90px; text-align: center;
  }

  .facts {
    position: absolute; top: 646px; left: 0; width: 700px;
    font-family: "Roboto Condensed", sans-serif; color: var(--ink-soft);
  }
  .fact { position: absolute; width: 180px; text-align: center; }
  .fact-volume { left: 166px; }
  .fact-alcohol { left: 352px; }
  .fact-title { font-size: 17px; font-weight: 400; letter-spacing: -0.3px; }
  .fact-value { font-size: 33px; font-weight: 300; line-height: 1.2; letter-spacing: -0.5px; }

  .maker {
    position: absolute; top: 742px; left: 0; width: 700px; text-align: center;
    font-family: "Oswald", sans-serif; font-weight: 400;
    font-size: 11px; letter-spacing: 6px; color: var(--ink-soft);
  }
</style>
</head>
<body>
<main class="canvas">
  <section class="label" aria-label="TONVALE Phantom Batch K7 bottle label">
    <div class="label-paper"></div>

    <svg class="frame-lines" viewBox="0 0 700 843" aria-hidden="true">
      <g stroke="var(--rule)" stroke-width="1.4" fill="none">
        <line x1="88" y1="52" x2="612" y2="52"/>
        <line x1="110" y1="62" x2="590" y2="62"/>
        <line x1="88" y1="792" x2="612" y2="792"/>
        <line x1="110" y1="781" x2="590" y2="781"/>
        <line x1="64" y1="112" x2="64" y2="728"/>
        <line x1="74" y1="130" x2="74" y2="710"/>
        <line x1="636" y1="112" x2="636" y2="728"/>
        <line x1="626" y1="130" x2="626" y2="710"/>
      </g>
    </svg>

    <div class="brand">
      <span class="brand-dot"></span>
      <div class="brand-name">TONVALE</div>
    </div>

    <h1 class="edition"><span>Phantom</span><span>Batch</span></h1>
    <div class="batch-badge">K7</div>

    <div class="facts">
      <div class="fact fact-volume">
        <div class="fact-title">Filling Volume</div>
        <div class="fact-value">0.5 liters</div>
      </div>
      <div class="fact fact-alcohol">
        <div class="fact-title">Alcohol Content</div>
        <div class="fact-value">43% vol.</div>
      </div>
    </div>

    <p class="maker">Destilled &amp; Bottled By Old Mariner</p>
  </section>
</main>
</body>
</html>
```